Can You Help Sell Glass Cabinets with a Banner Ad?

Our New Zealand-based company designs and sells glass cabinets and display cases. 75% of our customers are other businesses who want to display products in their shop or showroom. The other 25% of our customers are householders who want a glass cabinet for their personal collectables. We have been trading 2 years now, and are expanding rapidly. Our website address is www.vitrinaplace.example.nz.
We have made a strategic decision to focus on online advertising this year. This is because we want to raise our profile to the greatest number of and widest range of people. For now, this means banner advertising on high traffic New Zealand-based websites in an attempt to generate more traffic to our website. The websites we will initially use are www.ploverpost.example.nz and www.tuidaily.example.nz.
We therefore need a set of eye-catching banner ads designed for our online marketing campaign. The three banners required will probably just be variations on a single design.

Banner 1: Top Banner
760x120

Banner 2: Skyscraper
160x600

Banner 3: Medium Rectangle
300x250

Target Market(s)

The primary target market will be retailers who have shops and showrooms. They may not yet know they need a showcase.

Industry/Entity Type

Advertising

Requirements
Must have
• Vitrina Place logo
"High quality glass cabinets and showcases"
Maybe also "Show your products, not the cabinet"
[Corporate colour is green, as per logo. Secondary colours are orange, purple and grey.]
[Please use New Zealand (British) spelling]

Nice to have
• Please view our website and brochure on the Resources page for the look and feel of our company. In particular we like our logo, so it is possible you can take a lead from this. The logo emblem is designed to be evocative of glass.
The logo spot colour is 41,0,70,10.

```html
<!DOCTYPE html>
<html lang="en-NZ">
<head>
<meta charset="utf-8">
<title>Vitrina Place – banner variations</title>
<link rel="stylesheet" href="https://fonts.googleapis.com/css2?family=Lato:wght@400;700&family=PT+Sans&family=Roboto+Condensed&display=swap">
<style>
  :root {
    --page: #ffffff;
    --frame: #c9781e;
    --frame-light: #f2a94a;
    --orange: #f7a33c;
    --orange-deep: #e8902a;
    --orange-dark: #c6791f;
    --strip: #d98522;
    --red: #e8202a;
    --white: #ffffff;
    --mark: #b5cdb0;
    --glass-photo: #dfe5e8;
    --room-photo: #c33b3f;
    --stair-photo: #a0643a;
    --shop-photo: #8c8ea4;
  }
  * { box-sizing: border-box; margin: 0; padding: 0; }
  html, body { width: 1200px; height: 536px; overflow: hidden; background: var(--page); }
  .canvas { position: relative; width: 1200px; height: 536px; }

  .banner {
    position: absolute;
    border-radius: 14px;
    background: linear-gradient(180deg, var(--frame-light), var(--frame));
    box-shadow: 0 3px 6px rgba(0,0,0,.3);
  }
  .banner--plain { left: 12px; top: 58px; width: 1176px; height: 186px; }
  .banner--accent { left: 8px; top: 300px; width: 1180px; height: 190px; }

  .brand-panel {
    position: absolute; left: 4px; top: 4px;
    width: 506px; height: 126px;
    border-radius: 11px 0 0 0;
    background: linear-gradient(180deg, var(--orange) 0%, var(--orange-deep) 100%);
  }
  .brand {
    position: absolute; left: 22px; top: 34px;
    display: flex; align-items: center; gap: 18px;
  }
  .brand-square { width: 60px; height: 60px; background: var(--mark); }
  .brand-name {
    font-family: "Lato", sans-serif; font-weight: 700;
    font-size: 36px; letter-spacing: .5px; color: var(--white);
    line-height: 1;
  }
  .brand-line {
    font-family: "Lato", sans-serif; font-weight: 400;
    font-size: 23px; color: var(--white); margin-top: 6px;
  }

  .tagline {
    position: absolute; left: 4px; top: 135px;
    width: 510px; height: 46px;
    display: flex; align-items: center; padding-left: 14px;
    font-family: "PT Sans", sans-serif; font-size: 29px; color: var(--white);
    text-shadow: 1px 1px 2px rgba(0,0,0,.35);
    border-radius: 0 0 0 11px;
    background: linear-gradient(90deg, var(--strip), var(--orange-dark));
  }
  .banner--accent .tagline { top: 140px; width: 507px; padding-left: 10px; background: var(--red); }

  .gallery {
    position: absolute; left: 514px; top: 4px; right: 4px; bottom: 4px;
    border-radius: 0 11px 11px 0;
    background: var(--orange-dark);
  }
  .photo { position: absolute; top: 1px; height: 125px; border: 1px solid rgba(255,255,255,.6); }
  .photo--cabinet { left: 6px; width: 62px; background: linear-gradient(180deg, #f1f4f5, var(--glass-photo)); }
  .photo--counter { left: 75px; width: 174px; background: linear-gradient(180deg, #eceaea 0%, #e6e2e2 45%, var(--room-photo) 75%, #9b2328 100%); }
  .photo--stairs { left: 256px; width: 142px; background: linear-gradient(135deg, #e8e4dc 0%, var(--stair-photo) 70%); }
  .photo--shop { left: 404px; width: 242px; height: 164px; background: linear-gradient(180deg, #e9eef2 0%, var(--shop-photo) 55%, #4d5160 100%); }
  .banner--accent .photo--cabinet { left: 6px; width: 66px; height: 128px; }
  .banner--accent .photo--counter { left: 78px; width: 172px; height: 128px; }
  .banner--accent .photo--stairs { left: 257px; width: 141px; height: 128px; }
  .banner--accent .photo--shop { left: 405px; width: 239px; height: 166px; }

  .promise {
    position: absolute; left: 10px; top: 130px; width: 380px;
    text-align: center;
    font-family: "Roboto Condensed", sans-serif; font-size: 24px; line-height: 22px;
    color: var(--white); text-shadow: 1px 1px 2px rgba(0,0,0,.4);
  }
  .banner--accent .promise { top: 133px; }
</style>
</head>
<body>
<div class="canvas">

  <section class="banner banner--plain" aria-label="Vitrina Place top banner, orange tagline">
    <div class="brand-panel">
      <div class="brand">
        <span class="brand-square"></span>
        <div>
          <div class="brand-name">VITRINA PLACE</div>
          <div class="brand-line">design strength value</div>
        </div>
      </div>
    </div>
    <p class="tagline">Show your products, not the cabinet</p>
    <div class="gallery">
      <div class="photo photo--cabinet" role="img" aria-label="Tall glass display tower with shelves"></div>
      <div class="photo photo--counter" role="img" aria-label="Glass counter showcase in a red and white showroom"></div>
      <div class="photo photo--stairs" role="img" aria-label="Glass cabinet in a hallway beside a wooden staircase"></div>
      <div class="photo photo--shop" role="img" aria-label="Retail shop interior fitted with glass display cases"></div>
      <p class="promise">High quality&nbsp; glass cabinets&nbsp; and showcases</p>
    </div>
  </section>

  <section class="banner banner--accent" aria-label="Vitrina Place top banner, red tagline">
    <div class="brand-panel">
      <div class="brand">
        <span class="brand-square"></span>
        <div>
          <div class="brand-name">VITRINA PLACE</div>
          <div class="brand-line">design strength value</div>
        </div>
      </div>
    </div>
    <p class="tagline">Show your products, not the cabinet</p>
    <div class="gallery">
      <div class="photo photo--cabinet" role="img" aria-label="Tall glass display tower with shelves"></div>
      <div class="photo photo--counter" role="img" aria-label="Glass counter showcase in a red and white showroom"></div>
      <div class="photo photo--stairs" role="img" aria-label="Glass cabinet in a hallway beside a wooden staircase"></div>
      <div class="photo photo--shop" role="img" aria-label="Retail shop interior fitted with glass display cases"></div>
      <p class="promise">High quality&nbsp; glass cabinets&nbsp; and showcases</p>
    </div>
  </section>

</div>
</body>
</html>
```